Social Media Graphics - Harbor Climb REVISED

Create 6-7 individual social media graphics (square size) to encourage folks to join our online course called:

The Lantern Ledger Plan
How to Launch a Multi-Million Business From Scratch
Sign Up Today!

IMPORTANT: Make the largest and most prominent text on the graphic be: How to Launch a Multi-Million Business From Scratch

For the color scheme of the graphics, let's try a blue color palette; make sure the graphics appeal to both men and women

Make sure each graphic contains 1 of the 3 pics attached (crop pic as needed); and make sure one of the graphics is all TEXT only.

Target Market(s)

men and women looking to start a business

Industry/Entity Type

Entrepreneurship

Colors
0054AA
0677BA
7BADD7
CADEEF
E8F1F8

Requirements
Must have
• All the text and use the 3 pics provided; one graphic can be all text; Simple, modern design that's easy to read

```html
<!DOCTYPE html>
<html lang="en">
<head>
<meta charset="utf-8">
<title>The Lantern Ledger Plan – Sign Up</title>
<link rel="stylesheet" href="https://fonts.googleapis.com/css2?family=Work+Sans:wght@400;600;700&family=Archivo+Black&display=swap">
<style>
  :root {
    --blue-deep: #0054AA;
    --blue-mid: #0677BA;
    --blue-soft: #7BADD7;
    --blue-pale: #CADEEF;
    --blue-mist: #E8F1F8;
    --navy: #08306a;
    --ring: #0a2f63;
    --photo-warm: #c9a48e;
    --photo-cool: #3c4a6a;
    --text: #ffffff;
  }
  html, body {
    margin: 0;
    padding: 0;
    width: 1200px;
    height: 1200px;
    overflow: hidden;
  }
  .post {
    position: relative;
    width: 1200px;
    height: 1200px;
    background: linear-gradient(100deg, var(--blue-mid) 0%, var(--blue-deep) 50%, var(--navy) 100%);
    overflow: hidden;
    font-family: "Work Sans", Arial, sans-serif;
    color: var(--text);
  }
  .post-art {
    position: absolute;
    inset: 0;
  }
  .course-title {
    position: absolute;
    top: 764px;
    left: 0;
    width: 100%;
    margin: 0;
    text-align: center;
    font-weight: 600;
    font-size: 44px;
    line-height: 52px;
    letter-spacing: 0.5px;
    color: var(--blue-mist);
  }
  .course-tagline {
    position: absolute;
    top: 834px;
    left: 0;
    width: 100%;
    margin: 0;
    text-align: center;
    font-weight: 700;
    font-size: 62px;
    line-height: 72px;
    letter-spacing: 0;
  }
  .call-to-action {
    position: absolute;
    top: 1010px;
    left: 0;
    width: 100%;
    margin: 0;
    text-align: center;
    font-family: "Archivo Black", "Arial Black", sans-serif;
    font-size: 56px;
    line-height: 1;
    color: var(--blue-pale);
  }
</style>
</head>
<body>
<main class="post">
  <svg class="post-art" width="1200" height="1200" viewBox="0 0 1200 1200">
    <defs>
      <radialGradient id="photo-fill" cx="50%" cy="42%" r="60%">
        <stop offset="0%" stop-color="var(--photo-warm)"/>
        <stop offset="55%" stop-color="#8f6f6a"/>
        <stop offset="100%" stop-color="var(--photo-cool)"/>
      </radialGradient>
      <linearGradient id="dot-fade" x1="0" y1="0" x2="0" y2="1">
        <stop offset="0" stop-color="var(--blue-pale)" stop-opacity="0.5"/>
        <stop offset="1" stop-color="var(--blue-pale)" stop-opacity="0.3"/>
      </linearGradient>
    </defs>

    <g class="dot-grid" fill="url(#dot-fade)">
      <circle cx="451" cy="36" r="10"/><circle cx="501" cy="36" r="10"/><circle cx="551" cy="36" r="10"/><circle cx="601" cy="36" r="10"/><circle cx="651" cy="36" r="10"/><circle cx="701" cy="36" r="10"/><circle cx="751" cy="36" r="10"/>
      <circle cx="451" cy="87" r="10"/><circle cx="501" cy="87" r="10"/><circle cx="551" cy="87" r="10"/><circle cx="601" cy="87" r="10"/><circle cx="651" cy="87" r="10"/><circle cx="701" cy="87" r="10"/><circle cx="751" cy="87" r="10"/>
      <circle cx="451" cy="138" r="10"/><circle cx="501" cy="138" r="10"/><circle cx="551" cy="138" r="10"/><circle cx="601" cy="138" r="10"/><circle cx="651" cy="138" r="10"/><circle cx="701" cy="138" r="10"/><circle cx="751" cy="138" r="10"/>
    </g>

    <polygon class="arrow-large" points="1009,378 1170,469 1009,561" fill="var(--blue-soft)"/>
    <polygon class="arrow-small" points="868,400 984,469 868,536" fill="var(--blue-pale)" opacity="0.6"/>

    <circle class="photo-ring" cx="600" cy="412" r="322" fill="var(--ring)" opacity="0.85"/>
    <circle class="host-photo" cx="600" cy="412" r="289" fill="url(#photo-fill)" role="img" aria-label="Photo of the two course hosts smiling in front of framed artwork"/>
  </svg>

  <h1 class="course-title">The Lantern Ledger Plan</h1>
  <p class="course-tagline">How to Launch a Multi-Million<br>Business From Scratch</p>
  <p class="call-to-action">Sign Up Today!</p>
</main>
</body>
</html>
```